Korean Homemade food restaurant just like what your mom cooks at home

I need a black and white simple and modern design according to my logo.
My restaurant name is Noru Kan (meaning of home cooking).
I need to have 솔찬(Noru Kan) in Korean need to be included. Once again 솔찬.
I am not sure if I need to include my name and number and adress.

솔찬 Noru Kan 418 Marlow Ct. Clarksville, TN 37512 Grant Oh Owner Cell:931-555-0183 Store:931-555-0297

Target Market(s)

business owners, university students

Industry/Entity Type

Restaurant

Contact Information for Business Card

This is traditional Korean food restaurant that targets university students during lunch and Korean business travelers at dinner.

Font styles to use
Sans Serif

Requirements
Must have
• Must have my logo.

```html
<!DOCTYPE html>
<html lang="en">
<head>
<meta charset="utf-8">
<title>Noru Kan – Business Card</title>
<link href="https://fonts.googleapis.com/css2?family=Arimo:wght@400;700&family=Noto+Sans+KR:wght@300;400&display=swap" rel="stylesheet">
<style>
  :root {
    --page: #e9e7e3;
    --card: #ffffff;
    --card-shade: #f1f1f1;
    --ink: #111111;
    --band: #0b0b0b;
    --band-text: #e6e6e6;
  }
  * { box-sizing: border-box; margin: 0; padding: 0; }
  html, body {
    width: 1200px; height: 885px; overflow: hidden;
    background: var(--page);
    font-family: "Arimo", Arial, sans-serif;
    color: var(--ink);
  }
  .stage {
    position: relative; width: 1200px; height: 885px;
    display: flex; justify-content: center; align-items: center; gap: 120px;
  }
  .card {
    position: relative;
    width: 320px; height: 560px;
    background: radial-gradient(ellipse at 50% 40%, var(--card) 55%, var(--card-shade) 100%);
    box-shadow: 0 6px 18px rgba(0,0,0,.18);
    overflow: hidden;
  }
  /* front */
  .card--front .brand-block {
    position: absolute; top: 120px; left: 0; right: 0;
    display: flex; justify-content: center; align-items: center; gap: 12px;
  }
  .brand-mark { width: 22px; height: 22px; background: var(--ink); border-radius: 50%; }
  .brand-name { font-weight: 700; font-size: 46px; letter-spacing: -1px; }
  .person { position: absolute; top: 255px; left: 0; right: 0; text-align: center; }
  .person-name { font-size: 32px; font-weight: 400; }
  .person-name strong { font-weight: 700; }
  .person-role { font-size: 18px; margin-top: 4px; }
  .contacts { position: absolute; top: 345px; left: 60px; list-style: none; }
  .contacts li { display: flex; align-items: center; gap: 12px; font-size: 22px; line-height: 30px; }
  .contacts svg { width: 16px; height: 16px; flex: none; }
  .address-band {
    position: absolute; left: 0; right: 0; bottom: 0; height: 112px;
    background: var(--band); color: var(--band-text);
    display: flex; flex-direction: column; justify-content: center; align-items: center;
    font-size: 19px; line-height: 26px; text-align: center;
  }
  /* back */
  .card--back .brand-stack {
    position: absolute; top: 200px; left: 0; right: 0;
    display: flex; flex-direction: column; align-items: center;
  }
  .card--back .brand-row { display: flex; align-items: center; gap: 12px; }
  .brand-name--large { font-size: 52px; }
  .brand-korean {
    margin-top: 14px;
    font-family: "Noto Sans KR", sans-serif; font-weight: 300;
    font-size: 40px; letter-spacing: 6px;
  }
</style>
</head>
<body>
<main class="stage">
  <section class="card card--front" aria-label="Card front">
    <div class="brand-block">
      <span class="brand-mark"></span>
      <span class="brand-name">Noru Kan</span>
    </div>
    <div class="person">
      <p class="person-name">Grant <strong>Oh</strong></p>
      <p class="person-role">Owner</p>
    </div>
    <ul class="contacts">
      <li>
        <svg viewBox="0 0 16 16" aria-label="Cell"><rect x="3" y="0.5" width="10" height="15" rx="2" fill="#111"/><rect x="5" y="2.5" width="6" height="8" fill="#fff"/><circle cx="8" cy="13" r="1" fill="#fff"/></svg>
        931-555-0183
      </li>
      <li>
        <svg viewBox="0 0 16 16" aria-label="Store"><rect x="0.5" y="2" width="15" height="12" rx="2" fill="#111"/><path d="M3 6 Q8 2 13 6" stroke="#fff" stroke-width="1.5" fill="none"/><circle cx="8" cy="10" r="2" fill="#fff"/></svg>
        931-555-0297
      </li>
    </ul>
    <footer class="address-band">
      <span>418 Marlow Ct. Clarksville,</span>
      <span>TN 37512</span>
    </footer>
  </section>

  <section class="card card--back" aria-label="Card back">
    <div class="brand-stack">
      <div class="brand-row">
        <span class="brand-mark"></span>
        <span class="brand-name brand-name--large">Noru Kan</span>
      </div>
      <p class="brand-korean" lang="ko">솔찬</p>
    </div>
  </section>
</main>
</body>
</html>
```